Sexy Flyer for Bra Sale

We a need flyer designed for promoting the brand Tarvel Apparel Company which has just begun selling bra's. need a flyer which can posted on Facebook and other social media websites. the flyer has to be attractive to girls/ladies between the ages 16 - 39. The company has been associated mainly with men's products and is now venturing into supplying bra's into the market. The tarvel company logo, the bra label design and the pictures of the bra's are attached.

Product description
Microfiber T-shirt bra with molded, lightly padded underwire cups for shaping and good support the bra also give's a fuller, uplifted shape and enhanced cleavage . Invisible seams for improved comfort. Narrow, adjustable shoulder straps and hook-and-eye fasteners at back. Available in two colors of Black & Black with Decorative Touches of Pink.

About Tarvel Apparel Company
The Tarvel Apparel Company was founded on the philosophy of design, quality and the ideals of redefining fashion. Sri Lanka is the global hub for manufacturing some of the most exclusive and fashionable products and the Tarvel brand aims at giving the Sri Lankan consumer access to high-quality, affordable and fashionable clothing from a trusted company and name. A company-wide devotion to high quality‚ honest values and timeless style with a twist. That’s authentic Tarvel. And that’s just what you’ll get‚ no matter your latitude or longitude. At Tarvel Apparel Company we constantly strive to build a culture just as inspiring as the people who wear our clothes…

Target Market(s)

Ladies Girls 16 -39
Selling Bra's

Industry/Entity Type

Womens Clothing

Requirements
Must have
• To be able to upload the flyer on Facebook and other social media platforms
• the flyer must include the Tarvel Apparel Company Logo
Nice to have
• Sexy flyer.

```html
<!DOCTYPE html>
<html lang="en">
<head>
<meta charset="utf-8">
<title>Microfiber T-shirt Bra – Tarvel Apparel Company</title>
<link rel="stylesheet" href="https://fonts.googleapis.com/css2?family=Pinyon+Script&family=Lobster&family=Arimo:wght@400;700&display=swap">
<style>
  :root {
    --red-hot: #f00808;
    --red-deep: #a30000;
    --maroon-band: #4a0606;
    --title-white: #ffffff;
    --outline-black: #111111;
    --bra-yellow: #ffff00;
    --photo-grey: #d9d3cc;
    --photo-dark: #2a2a2a;
    --ring-black: #000000;
  }
  * { margin: 0; padding: 0; box-sizing: border-box; }
  html, body { width: 790px; height: 1200px; overflow: hidden; }
  body { background: var(--red-deep); }

  .flyer {
    position: relative;
    width: 790px;
    height: 1200px;
    overflow: hidden;
    background: radial-gradient(ellipse 70% 60% at 52% 50%, var(--red-hot) 0%, #d80404 55%, var(--red-deep) 100%);
  }

  .headline { position: absolute; left: 0; top: 0; width: 790px; height: 440px; }
  .headline__product {
    font-family: "Pinyon Script", cursive;
    fill: var(--title-white);
    stroke: var(--outline-black);
    stroke-width: 1.5;
    paint-order: stroke;
  }
  .headline__type {
    font-family: "Pinyon Script", cursive;
    fill: var(--bra-yellow);
    stroke: #5a3a00;
    stroke-width: 2;
    paint-order: stroke;
  }

  .detail-views { position: absolute; left: 56px; top: 240px; width: 152px; }
  .detail-view {
    width: 152px; height: 152px;
    border-radius: 50%;
    border: 4px solid var(--ring-black);
    background: #ffffff;
    display: flex; align-items: center; justify-content: center;
    margin-bottom: 36px;
  }
  .detail-view__photo {
    width: 110px; height: 90px;
    border-radius: 6px;
    background: linear-gradient(180deg, var(--photo-grey) 0%, var(--photo-grey) 40%, var(--photo-dark) 41%, var(--photo-dark) 80%, var(--photo-grey) 81%);
  }

  .hero-photo {
    position: absolute; left: 260px; top: 440px;
    width: 480px; height: 500px;
    border-radius: 120px 120px 0 0;
    background: linear-gradient(180deg, var(--photo-grey) 0%, #cfc8bf 38%, var(--photo-dark) 42%, #1c1c1c 80%, #cfc8bf 84%, var(--photo-grey) 100%);
  }

  .feature-strap {
    position: absolute; left: 0; top: 996px; width: 790px;
    text-align: center;
    padding-right: 0;
    font-family: "Lobster", cursive;
    font-size: 40px;
    color: var(--bra-yellow);
  }
  .feature-strap span { display: inline-block; transform: translateX(-6px); }

  .benefits { position: absolute; left: 0; top: 1084px; width: 558px; }
  .benefit {
    height: 37px;
    margin-bottom: 16px;
    background: var(--maroon-band);
    color: #ffffff;
    font-family: "Arimo", Arial, sans-serif;
    font-size: 25px;
    line-height: 37px;
    text-align: center;
  }

  .brand-mark {
    position: absolute; left: 612px; top: 1070px; width: 150px;
    display: flex; flex-direction: column; align-items: center;
    font-family: "Arimo", Arial, sans-serif;
    font-weight: 700;
    color: #ffffff;
    text-align: center;
    line-height: 1.05;
  }
  .brand-mark__square { width: 40px; height: 40px; background: #ffffff; margin-bottom: 8px; }
  .brand-mark__name { font-size: 30px; }
  .brand-mark__sub { font-size: 15px; margin-top: 4px; }
</style>
</head>
<body>
<main class="flyer">
  <svg class="headline" viewBox="0 0 790 440" aria-label="Microfiber T-shirt Bra">
    <text class="headline__product" x="48" y="146" font-size="92" textLength="704" lengthAdjust="spacingAndGlyphs">Microfiber T-shirt</text>
    <text class="headline__type" x="264" y="402" font-size="270" textLength="440" lengthAdjust="spacingAndGlyphs">Bra</text>
  </svg>

  <section class="detail-views">
    <div class="detail-view"><div class="detail-view__photo" role="img" aria-label="Black bra with pink straps on a mannequin, front view"></div></div>
    <div class="detail-view"><div class="detail-view__photo" role="img" aria-label="All-black bra on a mannequin, front view"></div></div>
    <div class="detail-view"><div class="detail-view__photo" role="img" aria-label="Black and pink bra on a mannequin, back view with hook-and-eye fastener"></div></div>
    <div class="detail-view"><div class="detail-view__photo" role="img" aria-label="All-black bra on a mannequin, back view"></div></div>
  </section>

  <div class="hero-photo" role="img" aria-label="Black microfiber T-shirt bra with pink trim, straps and bow on a dress form"></div>

  <p class="feature-strap"><span>Adjustable Shoulder Straps</span></p>

  <ul class="benefits" style="list-style:none">
    <li class="benefit">Uplifted Shape and Enhanced Cleavage</li>
    <li class="benefit">Invisible seams for improved comfort</li>
  </ul>

  <div class="brand-mark">
    <div class="brand-mark__square"></div>
    <span class="brand-mark__name">tarvel</span>
    <span class="brand-mark__sub">apparel company</span>
  </div>
</main>
</body>
</html>
```